Local electrical company needs two flyers designed

We are a small local electrical contracting company and are in desperate need of a awasome flyer design to help grow our business

hi everyone.

please keep the logo off the front page.
it can go on the rear.

We are really trying to portray a angry/frustrated women BECAUSE her lights are broken.
not light globes

Target Market(s)

Home owners

Industry/Entity Type

Electrical

Font styles to use
Serif

Requirements
Nice to have

```html
<!DOCTYPE html>
<html lang="en">
<head>
<meta charset="utf-8">
<title>Bright Spark Electrical – Lighting Offer Flyer</title>
<link href="https://fonts.googleapis.com/css2?family=Arvo:wght@700&family=Open+Sans:ital,wght@0,400;0,700;1,400&family=Roboto+Condensed:ital,wght@0,700;1,800&display=swap" rel="stylesheet">
<style>
  :root {
    --page: #ebe7e1;
    --ink: #1b1b1b;
    --white: #ffffff;
    --navy: #232a6e;
    --band-top: #1f57b5;
    --band-bottom: #0d1f6a;
    --yellow: #f4e01a;
    --tick-red: #c4141b;
    --quote-grey: #b5b5b5;
    --name-red: #c4141b;
    --rule-blue: #3b4aa0;
    --brand-orange: #e07a16;
    --card-light: #ffffff;
    --card-shade: #e6e6e6;
  }
  * { margin: 0; padding: 0; box-sizing: border-box; }
  html, body { width: 1200px; height: 506px; overflow: hidden; }
  body { background: var(--page); position: relative; font-family: "Open Sans", Arial, sans-serif; color: var(--ink); }

  .flyer { position: absolute; width: 548px; height: 390px; overflow: hidden; box-shadow: 0 3px 8px rgba(0,0,0,.35); }
  .flyer--front { left: 32px; top: 38px; }
  .flyer--back { left: 618px; top: 84px; background: linear-gradient(180deg, var(--card-light) 0%, #f4f4f4 55%, var(--card-shade) 100%); }

  /* front */
  .front-photo { position: absolute; inset: 0 0 64px 0;
    background: linear-gradient(180deg, #1a1a1a 0%, #3f3f3f 22%, #5a5a5a 36%, #a9a9a9 48%, #c6c6c6 75%, #d2d2d2 100%); }
  .front-photo::after { content: ""; position: absolute; right: 28px; top: 95px; width: 230px; height: 231px;
    border-radius: 46% 46% 0 0; background: linear-gradient(180deg, #5a3a2c, #5c3a78); opacity: .55; }
  .front-kicker { position: absolute; top: 12px; left: 0; right: 0; text-align: center; color: var(--white);
    font: 700 25px "Roboto Condensed", Arial, sans-serif; text-shadow: 0 2px 3px rgba(0,0,0,.6); }
  .front-headline { position: absolute; top: 43px; left: 0; right: 0; text-align: center; color: var(--white);
    font: 700 27px "Roboto Condensed", Arial, sans-serif; text-shadow: 0 2px 3px rgba(0,0,0,.7); }
  .front-question { position: absolute; left: 46px; top: 274px; color: var(--navy); font: 700 21px "Arvo", Georgia, serif; }
  .offer-band { position: absolute; left: 0; right: 0; bottom: 0; height: 64px;
    background: linear-gradient(180deg, var(--band-top), var(--band-bottom)); border-top: 3px solid #cfd3dc;
    display: flex; align-items: center; justify-content: center; }
  .offer-band__text { color: var(--yellow); font: italic 800 31px "Roboto Condensed", Arial, sans-serif; text-shadow: 1px 2px 2px rgba(0,0,0,.6); white-space: nowrap; }

  /* back */
  .call-label { position: absolute; left: 34px; width: 208px; top: 28px; text-align: center; font: 700 25px "Roboto Condensed", Arial, sans-serif; }
  .call-rule { position: absolute; left: 34px; top: 61px; width: 208px; height: 2px; background: var(--rule-blue); }
  .call-number { position: absolute; left: 50px; top: 66px; display: flex; align-items: center; gap: 4px; font: 700 27px "Roboto Condensed", Arial, sans-serif; }
  .benefits { list-style: none; position: absolute; left: 24px; top: 116px; }
  .benefits li { display: flex; align-items: flex-start; gap: 6px; font: 700 17px/21px "Open Sans", Arial, sans-serif; color: #2a2a2a; margin-bottom: 20px; }
  .benefits li:nth-child(3) { margin-bottom: 18px; }
  .benefits svg { flex: none; margin-top: 2px; }

  .brand { position: absolute; left: 350px; top: 160px; width: 190px; display: flex; align-items: center; gap: 6px;
    font: 700 17px "Roboto Condensed", Arial, sans-serif; color: var(--brand-orange); }
  .brand__dot { width: 14px; height: 14px; border-radius: 50%; background: var(--brand-orange); flex: none; }

  .testimonial { position: absolute; left: 290px; top: 200px; width: 244px; }
  .testimonial__mark { position: absolute; font: 700 48px/1 Georgia, serif; color: var(--quote-grey); }
  .testimonial__mark--open { left: 0; top: -8px; }
  .testimonial__mark--close { left: 140px; top: 56px; }
  .testimonial__text { font: italic 400 9.4px/13px "Open Sans", Arial, sans-serif; color: #333; text-indent: 26px; }
  .testimonial__author { position: absolute; right: 12px; top: 80px; font: 700 10.5px "Open Sans", Arial, sans-serif; color: var(--name-red); }
  .web { position: absolute; right: 22px; top: 303px; display: flex; align-items: center; gap: 4px; font: 700 12.5px "Open Sans", Arial, sans-serif; color: var(--navy); }

  .info-band { position: absolute; left: 0; right: 0; bottom: 0; height: 66px;
    background: linear-gradient(180deg, var(--band-top), var(--band-bottom)); border-top: 3px solid #cfd3dc; }
  .payments { position: absolute; left: 24px; top: 12px; width: 130px; height: 38px; background: var(--white); border-radius: 3px;
    display: flex; align-items: center; justify-content: space-around; padding: 0 6px;
    font: 400 11px "Open Sans", Arial, sans-serif; color: #444; }
  .terms { position: absolute; left: 303px; top: 12px; color: var(--white); font: 400 9.6px/12px "Open Sans", Arial, sans-serif; }
  .terms p + p { margin-top: 6px; }
</style>
</head>
<body>

<section class="flyer flyer--front">
  <div class="front-photo" role="img" aria-label="Photo of a frustrated woman clutching her head beside a dead light bulb hanging from the ceiling"></div>
  <p class="front-kicker">Is your lighting frustrating you?</p>
  <h1 class="front-headline">Tired of coming home to lights that dont work</h1>
  <p class="front-question">Thinking of a change?</p>
  <div class="offer-band"><p class="offer-band__text">SAVE $25 off your lighting replacement</p></div>
</section>

<section class="flyer flyer--back">
  <h2 class="call-label">Call now</h2>
  <div class="call-rule"></div>
  <p class="call-number">
    <svg width="24" height="24" viewBox="0 0 24 24" aria-hidden="true"><circle cx="12" cy="12" r="10.5" fill="none" stroke="#c4141b" stroke-width="1.6"/><path d="M9 6.5c-1.5.6-2 2.2-1.2 4.3 1 2.6 3.2 5 5.6 6.3 1.6.8 3 .5 3.5-.8l-2.2-1.8-1.2.9c-1.4-.8-2.6-2.2-3.2-3.8l1.1-.9L10.3 6.5z" fill="#c4141b"/></svg>
    1300 555 018
  </p>

  <ul class="benefits">
    <li><svg width="24" height="20" viewBox="0 0 24 20" aria-hidden="true"><path d="M1 11l5-2 3 5C13 7 18 3 23 1 17 6 12 12 9 19z" fill="var(--tick-red)"/></svg><span>Specialising in domestic<br>electrical repairs</span></li>
    <li><svg width="24" height="20" viewBox="0 0 24 20" aria-hidden="true"><path d="M1 11l5-2 3 5C13 7 18 3 23 1 17 6 12 12 9 19z" fill="var(--tick-red)"/></svg><span>On Time guarantee<br>or $100 OFF</span></li>
    <li><svg width="24" height="20" viewBox="0 0 24 20" aria-hidden="true"><path d="M1 11l5-2 3 5C13 7 18 3 23 1 17 6 12 12 9 19z" fill="var(--tick-red)"/></svg><span>Up front pricing</span></li>
    <li><svg width="24" height="20" viewBox="0 0 24 20" aria-hidden="true"><path d="M1 11l5-2 3 5C13 7 18 3 23 1 17 6 12 12 9 19z" fill="var(--tick-red)"/></svg><span>No mess guaranteed</span></li>
  </ul>

  <div class="brand"><span class="brand__dot"></span><span>Bright Spark Electrical</span></div>

  <blockquote class="testimonial">
    <span class="testimonial__mark testimonial__mark--open">&ldquo;</span>
    <p class="testimonial__text">Talk about great service! I called up to ask about fitting a light and they were here within half an hour and were able to fit it that afternoon. Good price and great service. I would not hesitate to recommend them.</p>
    <span class="testimonial__mark testimonial__mark--close">&rdquo;</span>
    <cite class="testimonial__author">— R.Hale Marrick Vale</cite>
  </blockquote>

  <p class="web">
    <svg width="11" height="11" viewBox="0 0 12 12" aria-hidden="true"><g fill="none" stroke="var(--navy)" stroke-width="1.1"><circle cx="6" cy="6" r="5"/><ellipse cx="6" cy="6" rx="2.2" ry="5"/><path d="M1 6h10"/></g></svg>
    www.brightsparkelectrical.com.au
  </p>

  <div class="info-band">
    <div class="payments"><span>Tallow</span><span>Orbit</span><span>Quill</span></div>
    <div class="terms">
      <p>*Mention this offer when you book your job<br>to receive offer. Limit one per household</p>
      <p>*Cannot be combined with any other offer</p>
    </div>
  </div>
</section>

</body>
</html>
```